Software company specialized in data analytics and professional services

We need a landing page design for our business. It should include our logo design. It should have multiple sections :
- stylish head
- what we do (data analytics software, professional services)
- contact form

Target Market(s)

Companies, B2B

Industry/Entity Type

Data

Number of Pages Required

1 page

Font styles to use
Sans Serif

Requirements
Must have
• Dark theme
Should not have
• Gradients on buttons

```html
<!DOCTYPE html>
<html lang="en">
<head>
<meta charset="utf-8">
<title>Data Analytics Landing Page</title>
<link href="https://fonts.googleapis.com/css2?family=DM+Sans:wght@400;500;700&family=Montserrat:wght@600;700&display=swap" rel="stylesheet">
<style>
:root{
  --backdrop:#23222d;
  --page:#0f1629;
  --section:#152038;
  --surface:#1b2746;
  --blue:#4a7be6;
  --heading:#eef2ff;
  --text:#a9b3cc;
  --muted:#7d88a5;
  --line:#2e3c62;
  --white:#ffffff;
  --cyan:#18c4d8;
}
*{box-sizing:border-box;margin:0;padding:0}
html,body{width:1200px;height:1200px;overflow:hidden;background:var(--backdrop);font-family:"DM Sans",sans-serif;color:var(--heading)}
.page{position:absolute;left:465px;top:62px;width:535px;height:1767px;background:var(--page);transform:scale(.6211);transform-origin:0 0;overflow:hidden}
.abs{position:absolute}
.p{font-size:3.6px;line-height:5.6px;color:var(--text)}
.eyebrow{font-size:5px;letter-spacing:1.6px;color:var(--text);text-transform:uppercase}
.h2{font-size:17px;line-height:17px;font-weight:500;color:var(--heading)}
.btn{background:var(--blue);color:var(--white);font-size:3.6px;font-weight:700;text-align:center;letter-spacing:.4px;border-radius:2px}
.topbar{left:0;top:0;width:535px;height:19px;background:var(--page);border-bottom:1px solid var(--line)}
.topbar-info{left:0;top:0;width:288px;height:19px;background:var(--blue);color:var(--white);font-size:4px;display:flex;align-items:center;gap:6px;padding-left:60px}
.topbar-info svg{width:5px;height:5px}
.topbar-info .sep{width:1px;height:10px;background:rgba(255,255,255,.5)}
.quote-btn{left:423px;top:3px;width:52px;height:12px;line-height:12px}
.hero{left:0;top:19px;width:535px;height:260px;background:var(--section)}
.hero-word{font-size:40px;line-height:44px;font-weight:700;color:var(--heading);letter-spacing:-.5px}
.vertical{font-size:3.6px;letter-spacing:1px;color:var(--text);writing-mode:vertical-rl;transform:rotate(180deg)}
.side-tab{left:522px;top:88px;width:13px;height:52px;background:var(--blue);border-radius:2px 0 0 2px;color:var(--white);font-size:3.4px;writing-mode:vertical-rl;transform:rotate(180deg);text-align:center;line-height:13px}
.stat-title{font-size:4px;font-weight:700;letter-spacing:.8px;color:var(--heading)}
.card{width:104px;height:130px;background:var(--surface);box-shadow:0 4px 14px rgba(0,0,0,.3);text-align:center;padding-top:58px}
.card-icon{position:absolute;left:36px;top:14px;width:30px;height:30px;border-radius:50%;background:var(--line)}
.card h4{font-size:4.6px;letter-spacing:1.2px;font-weight:700;margin-bottom:8px}
.card .p{padding:0 12px}
.step-dot{width:11px;height:11px;border-radius:50%;background:var(--blue);color:var(--white);font-size:3.4px;text-align:center;line-height:11px}
.step h4{font-size:4.6px;letter-spacing:1.2px;font-weight:700;text-align:center;margin-bottom:6px}
.step .p{text-align:center;color:var(--muted)}
.svc-icon{width:14px;height:14px;border-radius:50%;background:var(--surface);border:1px solid var(--line)}
.svc h4{font-size:4.6px;letter-spacing:1.2px;font-weight:700;margin-bottom:4px}
.svc .p{width:82px;color:var(--muted)}
.banner{left:60px;top:1218px;width:415px;height:83px;background:var(--blue);border-radius:3px;color:var(--white);padding:10px 15px}
.banner h3{font-size:16px;line-height:19px;font-weight:500}
.banner .p{color:var(--white);width:205px;margin-top:2px;font-size:4.2px;line-height:5.4px}
.banner-btn{display:block;width:52px;height:11px;margin-top:6px;background:var(--white);color:var(--blue);font-size:3.6px;font-weight:700;text-align:center;line-height:11px;border-radius:1px}
.form-card{left:302px;top:1272px;width:173px;height:231px;background:var(--surface);border-radius:12px 12px 3px 3px;box-shadow:0 4px 16px rgba(0,0,0,.35);padding:17px 13px 0 15px}
.field-label{font-size:3.8px;color:var(--heading);margin:4px 0 2px}
.field{height:13px;border:1px solid var(--line);background:var(--page);border-radius:2px;font-size:3.6px;color:var(--muted);padding-left:3px;line-height:11px;margin-bottom:3px;position:relative}
.field.area{height:22px}
.form-btn{width:64px;height:13px;line-height:13px;border-radius:7px;margin-top:6px}
.touch-title{font-size:15px;line-height:18px;font-weight:500;color:var(--heading)}
.feature-icon{width:20px;height:20px;border-radius:50%;background:var(--blue)}
.feature h4{font-size:5px;font-weight:700;margin-bottom:2px}
.feature .p{width:190px}
.cta-title{font-family:"Montserrat",sans-serif;font-size:15px;line-height:17.5px;font-weight:600;color:var(--heading)}
.cta-btn{width:44px;height:11px;line-height:11px;border-radius:6px}
.footer{left:0;top:1712px;width:535px;height:55px;background:var(--blue)}
.social{width:7px;height:7px;border-radius:50%;background:var(--white)}
.copyright{font-size:4.2px;color:var(--white)}
</style>
</head>
<body>
<main class="page">

  <header class="abs topbar">
    <div class="abs topbar-info">
      <svg viewBox="0 0 10 10"><path d="M5 0a3.5 3.5 0 0 0-3.5 3.5C1.5 6 5 10 5 10s3.5-4 3.5-6.5A3.5 3.5 0 0 0 5 0zm0 5a1.4 1.4 0 1 1 0-2.8A1.4 1.4 0 0 1 5 5z" fill="#fff"/></svg>
      <span>XXX Dummy Address , FL 34965</span>
      <span class="sep"></span>
      <svg viewBox="0 0 10 10"><path d="M2 0l2 2.5-1 1.2a6 6 0 0 0 3.3 3.3l1.2-1L10 8l-1.3 1.7C4.5 10 0 5.5.3 1.3z" fill="#fff"/></svg>
      <span>+X XXX XXX XXXX</span>
    </div>
    <div class="abs btn quote-btn">GET A QUOTE</div>
  </header>

  <section class="abs hero">
    <svg class="abs" style="left:130px;top:20px" width="240" height="215" viewBox="0 0 240 215">
      <circle cx="120" cy="107" r="104" fill="none" stroke="#25335a" stroke-width=".8"/>
      <circle cx="120" cy="107" r="75" fill="none" stroke="#25335a" stroke-width=".8"/>
    </svg>
    <div class="abs vertical" style="left:50px;top:35px">#DATA ANALYTICS</div>
    <div class="abs vertical" style="left:478px;top:170px">#DATA ANALYTICS</div>
    <div class="abs side-tab">CONTACT US</div>

    <div class="abs" role="img" aria-label="Low-poly blue and teal data landscape illustration" style="left:125px;top:55px;width:233px;height:130px;border-radius:50%;background:radial-gradient(ellipse at 50% 50%,rgba(42,140,240,.85) 0%,rgba(24,191,214,.55) 45%,rgba(21,32,56,0) 72%)"></div>

    <div class="abs hero-word" style="left:69px;top:58px">DATA</div>
    <div class="abs hero-word" style="left:236px;top:138px">ANALYTICS</div>
    <div class="abs p" style="left:103px;top:124px">Be ready to make decisions</div>

    <div class="abs" style="left:339px;top:78px;width:6px;height:6px;border-radius:50%;background:var(--cyan);border:1.5px solid #bff1f7"></div>
    <div class="abs stat-title" style="left:356px;top:78px">01. BOUNCE RATE</div>
    <div class="abs p" style="left:356px;top:84px">Lorem ipsum dolor sit amet consectetur.</div>

    <div class="abs" style="left:198px;top:178px;width:6px;height:6px;border-radius:50%;background:var(--cyan);border:1.5px solid #bff1f7"></div>
    <div class="abs stat-title" style="left:130px;top:192px">02. RETURNING VISITORS</div>
    <div class="abs p" style="left:116px;top:198px">Lorem ipsum dolor sit amet consectetur.</div>
  </section>

  <div class="abs eyebrow" style="left:60px;top:305px">Data Analytics Software</div>
  <h2 class="abs h2" style="left:60px;top:317px">Data Analytics<br>Techniques with our<br>Systems.</h2>
  <p class="abs p" style="left:60px;top:374px;width:205px">Lorem ipsum dolor sit amet consectetur. Etiam amet sodales lacus tincidunt duis at diam. Ante et mus in eget sed etiam nisi pellentesque. Faucibus sit mauris eu viverra adipiscing quisque quisque. Nullam ac et lobortis aliquet et risus volutpat dictumst egestas. Eget sodales habitasse in diam et facilisis dui nisi blandit quis. Dignissim nibh mattis senectus ipsum sit diam ut. Vel porta diam ipsum nunc auctor vel. Tincidunt feugiat vel leo neque.</p>
  <p class="abs p" style="left:60px;top:418px;width:205px">Enim neque semper ornare penatibus suscipit consectetur. Eu placerat adipiscing viverra sit natoque sed. Tellus at sit euismod nunc nisl pharetra. Faucibus convallis senectus id fermentum ac leo. Gravida suspendisse sed vitae turpis eget sed placerat.</p>
  <div class="abs" role="img" aria-label="Illustration of two analysts working at a large dashboard monitor" style="left:292px;top:300px;width:186px;height:146px;border-radius:8px;background:linear-gradient(160deg,#2a3d6e,#4a7be6 70%,#3b5fcf)"></div>

  <div class="abs card" style="left:98px;top:480px"><div class="card-icon"></div><h4>DATA MONETIZATION</h4><p class="p">Enim neque semper ornare penatibus suscipit consectetur. Eu placerat adipiscing viverra sit natoque sed. Tellus at sit euismod nunc nisl pharetra. Faucibus convallis senectus id fermentum ac leo.</p></div>
  <div class="abs card" style="left:218px;top:480px"><div class="card-icon" style="background:var(--blue)"></div><h4>MANAGE ANALYTICS</h4><p class="p">Enim neque semper ornare penatibus suscipit consectetur. Eu placerat adipiscing viverra sit natoque sed. Tellus at sit euismod nunc nisl pharetra. Faucibus convallis senectus id fermentum ac leo.</p></div>
  <div class="abs card" style="left:333px;top:480px"><div class="card-icon"></div><h4>BUSINESS INTELLIGENCE</h4><p class="p">Enim neque semper ornare penatibus suscipit consectetur. Eu placerat adipiscing viverra sit natoque sed. Tellus at sit euismod nunc nisl pharetra. Faucibus convallis senectus id fermentum ac leo.</p></div>

  <svg class="abs" style="left:0;top:628px" width="535" height="376" viewBox="0 0 535 376" preserveAspectRatio="none">
    <path d="M0 8C40-2 80 0 120 18s80 30 120 0 80-25 130-8 100 20 165 20V376H0z" fill="#152038"/>
  </svg>
  <div class="abs eyebrow" style="left:60px;top:688px">About Our Company</div>
  <h2 class="abs h2" style="left:60px;top:702px">We Provides Realtime<br>Data Solutions.</h2>
  <p class="abs p" style="left:60px;top:747px;width:205px">Lorem ipsum dolor sit amet consectetur. Etiam amet sodales lacus tincidunt duis at diam. Ante et mus in eget sed etiam nisi pellentesque. Faucibus sit mauris eu viverra adipiscing quisque quisque. Nullam ac et lobortis aliquet et risus volutpat dictumst egestas. Eget sodales habitasse in diam et facilisis dui nisi blandit quis. Dignissim nibh mattis senectus ipsum sit diam ut. Vel porta diam ipsum nunc auctor vel. Tincidunt feugiat vel leo neque.</p>
  <p class="abs p" style="left:60px;top:790px;width:205px">Enim neque semper ornare penatibus suscipit consectetur. Eu placerat adipiscing viverra sit natoque sed. Tellus at sit euismod nunc nisl pharetra. Faucibus convallis senectus id fermentum ac leo. Gravida suspendisse sed vitae turpis eget sed placerat.</p>
  <div class="abs" role="img" aria-label="Illustration of two people reviewing realtime charts on a floating screen" style="left:302px;top:664px;width:175px;height:148px;border-radius:50% 45% 40% 48%;background:radial-gradient(circle at 55% 45%,#4a7be6,#2f4c8e 60%,#1d2a4d)"></div>

  <div class="abs eyebrow" style="left:0;width:535px;text-align:center;top:842px">Working Process</div>
  <h2 class="abs h2" style="left:0;width:535px;text-align:center;top:853px;font-size:16px">How We Works?</h2>
  <p class="abs p" style="left:145px;width:245px;text-align:center;top:876px">Enim neque semper ornare penatibus suscipit consectetur. Eu placerat adipiscing viverra sit natoque sed. Tellus at sit euismod nunc nisl pharetra. Faucibus convallis senectus id fermentum ac leo.</p>
  <svg class="abs" style="left:125px;top:909px" width="285" height="4" viewBox="0 0 285 4">
    <line x1="0" y1="2" x2="285" y2="2" stroke="#3a5086" stroke-width=".6"/>
    <path d="M66 .5l2 1.5-2 1.5M69 .5l2 1.5-2 1.5M72 .5l2 1.5-2 1.5M208 .5l2 1.5-2 1.5M211 .5l2 1.5-2 1.5M214 .5l2 1.5-2 1.5" stroke="#4a7be6" stroke-width=".7" fill="none"/>
  </svg>
  <div class="abs step-dot" style="left:120px;top:905px">01</div>
  <div class="abs step-dot" style="left:262px;top:905px">02</div>
  <div class="abs step-dot" style="left:404px;top:905px">03</div>
  <div class="abs step" style="left:75px;top:928px;width:100px"><h4>DATA FOR ALL YOUR PEOPLE</h4><p class="p">Enim neque semper ornare penatibus suscipit consectetur. Eu placerat adipiscing viverra sit natoque sed.</p></div>
  <div class="abs step" style="left:217px;top:928px;width:100px"><h4>A NEW BREED OF AI</h4><p class="p">Enim neque semper ornare penatibus suscipit consectetur. Eu placerat adipiscing viverra sit natoque sed.</p></div>
  <div class="abs step" style="left:359px;top:928px;width:100px"><h4>ANALYTICS BUSINESS</h4><p class="p">Enim neque semper ornare penatibus suscipit consectetur. Eu placerat adipiscing viverra sit natoque sed.</p></div>

  <div class="abs eyebrow" style="left:0;width:535px;text-align:center;top:1028px">Best Services</div>
  <h2 class="abs h2" style="left:0;width:535px;text-align:center;top:1039px;font-size:16px">Explore Our Data Services</h2>
  <p class="abs p" style="left:145px;width:245px;text-align:center;top:1061px">Enim neque semper ornare penatibus suscipit consectetur. Eu placerat adipiscing viverra sit natoque sed. Tellus at sit euismod nunc nisl pharetra. Faucibus convallis senectus id fermentum ac leo.</p>

  <div class="abs svc-icon" style="left:75px;top:1104px"></div>
  <div class="abs svc" style="left:97px;top:1104px"><h4>BIG DATA CONSULTING</h4><p class="p">Enim neque semper ornare penatibus suscipit consectetur. Eu placerat adipiscing viverra sit natoque sed.</p></div>
  <div class="abs svc-icon" style="left:212px;top:1104px"></div>
  <div class="abs svc" style="left:234px;top:1104px"><h4>MACHINE LEARNING</h4><p class="p">Enim neque semper ornare penatibus suscipit consectetur. Eu placerat adipiscing viverra sit natoque sed.</p></div>
  <div class="abs svc-icon" style="left:350px;top:1104px"></div>
  <div class="abs svc" style="left:372px;top:1104px"><h4>DATA ANALYTICS</h4><p class="p">Enim neque semper ornare penatibus suscipit consectetur. Eu placerat adipiscing viverra sit natoque sed.</p></div>
  <div class="abs svc-icon" style="left:75px;top:1166px"></div>
  <div class="abs svc" style="left:97px;top:1166px"><h4>COMPUTER VISION</h4><p class="p">Enim neque semper ornare penatibus suscipit consectetur. Eu placerat adipiscing viverra sit natoque sed.</p></div>
  <div class="abs svc-icon" style="left:212px;top:1166px"></div>
  <div class="abs svc" style="left:234px;top:1166px"><h4>INTERNET OF THINGS</h4><p class="p">Enim neque semper ornare penatibus suscipit consectetur. Eu placerat adipiscing viverra sit natoque sed.</p></div>
  <div class="abs svc-icon" style="left:350px;top:1166px"></div>
  <div class="abs svc" style="left:372px;top:1166px"><h4>ARTIFICIAL INTELLIGENCE</h4><p class="p">Enim neque semper ornare penatibus suscipit consectetur. Eu placerat adipiscing viverra sit natoque sed.</p></div>

  <section class="abs banner">
    <h3>Explore Our Data Services</h3>
    <p class="p">Lorem ipsum dolor sit amet consectetur. Velit mus ultricies augue lacus cras tellus pulvinar tincidunt dictum.</p>
    <span class="banner-btn">GET A QUOTE</span>
  </section>

  <h2 class="abs touch-title" style="left:60px;top:1318px">Get In Touch</h2>
  <p class="abs p" style="left:60px;top:1340px;width:205px;font-size:4.4px;line-height:6px">Lorem ipsum dolor sit amet consectetur. Velit mus ultricies augue lacus cras tellus pulvinar tincidunt dictum.</p>
  <div class="abs feature-icon" style="left:60px;top:1365px"></div>
  <div class="abs feature" style="left:88px;top:1365px"><h4>Experienced Team Member</h4><p class="p">Lorem ipsum dolor sit amet consectetur. Velit mus ultricies augue lacus cras tellus pulvinar tincidunt dictum. Ipsum etiam nibh volutpat dignissim turpis suscipit. Arcu volutpat sit aliquam aenean magna in.</p></div>
  <div class="abs feature-icon" style="left:60px;top:1411px"></div>
  <div class="abs feature" style="left:88px;top:1411px"><h4>Advance Technology</h4><p class="p">Lorem ipsum dolor sit amet consectetur. Velit mus ultricies augue lacus cras tellus pulvinar tincidunt dictum. Ipsum etiam nibh volutpat dignissim turpis suscipit. Arcu volutpat sit aliquam aenean magna in.</p></div>
  <div class="abs feature-icon" style="left:60px;top:1457px"></div>
  <div class="abs feature" style="left:88px;top:1457px"><h4>Emergency Cares</h4><p class="p">Lorem ipsum dolor sit amet consectetur. Velit mus ultricies augue lacus cras tellus pulvinar tincidunt dictum. Ipsum etiam nibh volutpat dignissim turpis suscipit. Arcu volutpat sit aliquam aenean magna in.</p></div>

  <form class="abs form-card">
    <div class="field">First Name</div>
    <div class="field-label">Email</div>
    <div class="field">Email Address</div>
    <div class="field-label">Phone</div>
    <div class="field">Country code + Phone Number</div>
    <div class="field-label">Company</div>
    <div class="field">Company Name</div>
    <div class="field-label">Primary Interest</div>
    <div class="field">Contract Manufacturing
      <svg class="abs" style="right:4px;top:5px" width="3" height="2" viewBox="0 0 3 2"><path d="M0 0h3L1.5 2z" fill="#a9b3cc"/></svg>
    </div>
    <div class="field-label">Message</div>
    <div class="field area"></div>
    <p class="p" style="font-size:2.6px;line-height:3.4px;color:var(--muted)">Lorem ipsum dolor sit amet consectetur. Tellus arcu condimentum ornare nibh scelerisque convallis cras. Rutrum elementum dignissim egestas et amet lobortis porta.</p>
    <div class="btn form-btn">CONTACT WITH US</div>
  </form>

  <div class="abs" role="img" aria-label="Illustration of a support specialist with headset and floating chat icons" style="left:50px;top:1525px;width:242px;height:242px;border-radius:48% 52% 45% 55%;background:linear-gradient(150deg,#3fd8d0 0%,#7d8bef 40%,#4a7be6 75%,#3a5fd3)"></div>
  <h2 class="abs cta-title" style="left:306px;top:1581px">Connect with our<br>Data Analytics<br>Software specialists<br>get the help you need</h2>
  <div class="abs btn cta-btn" style="left:306px;top:1661px">LET'S TALK</div>

  <footer class="abs footer">
    <div class="abs social" style="left:395px;top:13px"></div>
    <div class="abs social" style="left:408px;top:13px"></div>
    <div class="abs social" style="left:421px;top:13px"></div>
    <div class="abs social" style="left:434px;top:13px"></div>
    <div class="abs social" style="left:447px;top:13px"></div>
    <div class="abs social" style="left:460px;top:13px"></div>
    <div class="abs copyright" style="left:377px;top:28px">Copyright © 2023, All Rights Reserved.</div>
  </footer>
</main>
</body>
</html>
```